Rack Flyer for Willowmere Dementia

We need a rack flyer design providing information on services we offer, fees and relevant contact information. Using company branding (logo, font and colours). Must be provided in a format that is easily edited for ongoing use.

For DL size (99 x 210mm)

```html
<!DOCTYPE html>
<html lang="en">
<head>
<meta charset="utf-8">
<title>Willowmere Dementia – DL Rack Flyer</title>
<link href="https://fonts.googleapis.com/css2?family=Nunito+Sans:wght@400;600;700;800;900&family=Dancing+Script:wght@700&display=swap" rel="stylesheet">
<style>
  :root{
    --navy:#25216e;
    --navy-deep:#0e0c31;
    --gold:#f2a516;
    --orange:#f6a11c;
    --sky:#dcecf7;
    --paper:#ffffff;
    --stage:#e8e5e0;
    --ink-soft:#dcdcf0;
  }
  *{box-sizing:border-box;margin:0;padding:0}
  html,body{width:1200px;height:800px;overflow:hidden;background:var(--stage);font-family:"Nunito Sans",Arial,sans-serif}
  .sheet{position:relative;width:1200px;height:800px;display:flex;justify-content:center;align-items:center;gap:60px}
  .flyer{position:relative;width:330px;height:700px;overflow:hidden;box-shadow:0 6px 24px rgba(0,0,0,.18)}

  .brand{display:flex;align-items:center;gap:7px;font-weight:800;font-size:17px;letter-spacing:-.2px}
  .brand-dot{width:18px;height:18px;border-radius:50%;border:2.5px solid currentColor}

  /* front */
  .flyer--front{background:linear-gradient(180deg,var(--paper) 0%,var(--sky) 45%,#cfe3f1 100%)}
  .flyer--front .brand{position:absolute;top:52px;left:0;right:0;justify-content:center;color:var(--navy)}
  .headline{position:absolute;top:92px;left:0;right:0;text-align:center;color:var(--navy);line-height:1}
  .headline-line{display:block;font-weight:900;font-size:26px}
  .headline-script{display:block;font-family:"Dancing Script",cursive;font-size:72px;margin:-4px 0 -8px;color:var(--navy)}
  .front-photo{position:absolute;top:250px;left:0;width:330px;height:320px;
    background:linear-gradient(160deg,#cfe2ee 0%,#d9cfa6 45%,#e8c048 70%,#c9b98a 100%)}
  .wave{position:absolute;left:0;bottom:0;width:330px}
  .front-copy{position:absolute;top:548px;left:28px;right:28px;color:#fff;font-size:11px;line-height:1.45;text-align:justify}
  .contact{text-align:center;margin-top:12px}
  .contact-title{color:var(--orange);font-weight:800;font-size:12px;line-height:1.35}
  .contact-line{color:var(--ink-soft);font-size:10px;line-height:1.4}

  /* back */
  .flyer--back{background:var(--navy)}
  .back-photo{position:absolute;top:150px;left:0;width:330px;height:340px;
    background:linear-gradient(150deg,#4b4a86 0%,#8e8aa0 40%,#a49a92 65%,#5c5a66 100%)}
  .back-top{position:absolute;top:0;left:0;width:330px;height:230px;background:linear-gradient(180deg,var(--navy) 70%,rgba(37,33,110,0) 100%)}
  .flyer--back .brand{position:absolute;top:26px;left:22px;color:#fff;font-size:15px}
  .intro{position:absolute;top:62px;left:22px;right:22px;color:#fff;font-size:9.5px;line-height:1.42;text-align:justify}
  .services{position:absolute;top:188px;left:150px;right:14px;color:#fff}
  .section-title{color:var(--orange);font-weight:800;font-size:16px;line-height:1.25}
  .service-list{list-style:none;margin-top:4px;font-size:8.2px;line-height:1.35}
  .service-list li{padding-left:9px;position:relative}
  .service-list li::before{content:"";position:absolute;left:0;top:3.5px;width:4px;height:4px;background:var(--gold);border-radius:50%}

  .fees{position:absolute;top:468px;left:18px;right:18px;color:#fff}
  .fees .section-title{margin-left:60px}
  .fee-grid{display:grid;grid-template-columns:90px 90px 1fr;grid-template-rows:38px 38px;gap:6px;margin-top:4px}
  .fee{border:1.5px solid #fff;border-radius:8px;text-align:center;display:flex;flex-direction:column;justify-content:center;font-weight:800;font-size:7.6px;line-height:1.1;position:relative;padding:0 3px}
  .fee-price{font-size:14px;font-weight:900;line-height:1;margin-top:2px}
  .fee-price small{font-size:5.5px;font-weight:700}
  .fee--featured{grid-column:3;grid-row:1 / span 2;background:var(--gold);border-color:var(--gold);font-size:8.6px;padding:0 8px}
  .fee--featured .fee-price{font-size:16px;margin-top:4px}
  .fee-star{position:absolute;right:6px;bottom:5px;width:11px;height:11px}
  .fee-star--left{right:auto;left:5px;bottom:4px;fill:var(--gold)}
  .note{position:absolute;top:578px;left:22px;right:22px;color:#fff;font-size:8.4px;line-height:1.35;text-align:justify}
  .flyer--back .contact{position:absolute;top:644px;left:0;right:0;margin:0}
</style>
</head>
<body>
<main class="sheet">

  <section class="flyer flyer--front" aria-label="Flyer front">
    <div class="brand"><span class="brand-dot"></span>Willowmere Dementia</div>
    <h1 class="headline">
      <span class="headline-line">Navigating</span>
      <span class="headline-script">Dementia</span>
      <span class="headline-line">Together</span>
    </h1>
    <div class="front-photo" role="img" aria-label="Photo of an elderly couple walking together outdoors, smiling"></div>
    <svg class="wave" viewBox="0 0 330 300" height="300" aria-hidden="true">
      <defs>
        <linearGradient id="frontNavy" x1="0" y1="0" x2="0" y2="1">
          <stop offset="0" stop-color="#25216e"/>
          <stop offset="1" stop-color="#0e0c31"/>
        </linearGradient>
      </defs>
      <path d="M0 112 C120 95 235 62 330 0 L330 300 L0 300Z" fill="var(--gold)"/>
      <path d="M0 130 C125 112 240 82 330 24 L330 300 L0 300Z" fill="url(#frontNavy)"/>
    </svg>
    <div class="front-copy">
      <p>Navigating a diagnosis of dementia can be daunting. You likely have many questions, and it can be overwhelming trying to figure out where to turn to for answers and help. We want you to know that you are not alone in this journey.</p>
      <div class="contact">
        <p class="contact-title">To know more, please contact:</p>
        <p class="contact-line">www.willowmeredementia.bm</p>
        <p class="contact-line">hello@willowmeredementia.bm</p>
        <p class="contact-line">(441) 555 0142</p>
      </div>
    </div>
  </section>

  <section class="flyer flyer--back" aria-label="Flyer back">
    <div class="back-photo" role="img" aria-label="Photo of a smiling elderly woman seated, hands resting on a walking cane"></div>
    <div class="back-top"></div>
    <div class="brand"><span class="brand-dot"></span>Willowmere Dementia</div>
    <p class="intro">As the numbers of those living with dementia in Bermuda continue to rise placing greater demands on an already strained health care system, Willowmere's clinical and evidence based consultation services improve the safety, independence and quality of life of persons with dementia and their caregivers. Our goal is to assist clients to successfully age in place at home with the support of their family caregivers, to reduce the overall cost and burden of care for this vulnerable population.</p>

    <div class="services">
      <h2 class="section-title">Services Offered</h2>
      <ul class="service-list">
        <li>Comprehensive Dementia Assessment</li>
        <li>Cognitive/Perceptual Screening</li>
        <li>Home Safety Audit (home modifications and adaptive equipment advice)</li>
        <li>Caregiver Education &amp; Support</li>
        <li>Falls Prevention Strategies</li>
        <li>Personalised Care Planning</li>
        <li>Preparation for future disease progression</li>
        <li>Case Management</li>
        <li>Check-in/monitoring visits for clients with limited social support</li>
        <li>Cognitive Stimulation Therapy (group programs for clients with mild-moderate dementia)</li>
      </ul>
    </div>

    <svg class="wave" viewBox="0 0 330 300" height="300" aria-hidden="true">
      <path d="M0 50 C110 44 230 22 330 0 L330 300 L0 300Z" fill="var(--gold)"/>
      <path d="M0 62 C115 56 235 34 330 13 L330 300 L0 300Z" fill="var(--navy)"/>
    </svg>

    <div class="fees">
      <h2 class="section-title">Services Fees</h2>
      <div class="fee-grid">
        <div class="fee">Initial<br>Consultation<span class="fee-price">$180</span></div>
        <div class="fee">Comprehensive Dementia Assessment<span class="fee-price">$395</span>
          <svg class="fee-star fee-star--left" viewBox="0 0 24 24" aria-hidden="true"><path d="M12 2l3 7h7l-5.5 4.5 2 7.5-6.5-4.5-6.5 4.5 2-7.5L2 9h7z"/></svg>
        </div>
        <div class="fee fee--featured">Comprehensive Dementia Assessment &amp; ongoing case management services<span class="fee-price">$720</span>
          <svg class="fee-star" viewBox="0 0 24 24" fill="var(--navy)" aria-hidden="true"><path d="M12 2l3 7h7l-5.5 4.5 2 7.5-6.5-4.5-6.5 4.5 2-7.5L2 9h7z"/></svg>
        </div>
        <div class="fee">Monthly check in/<br>monitoring visits<span class="fee-price">$180</span></div>
        <div class="fee">Cognitive Stimulation Therapy<span class="fee-price">$500 <small>(per term)</small></span></div>
      </div>
    </div>

    <p class="note">We are pleased to share that services offered by Willowmere Dementia are currently covered under Harborline and Crestview health insurance plans. We also have availability of funding support for those in financial need who are unable to afford co-pay, enabling equitable access to these essential care and support services regardless of financial means.</p>

    <div class="contact">
      <p class="contact-title">To know more, please contact:</p>
      <p class="contact-line">www.willowmeredementia.bm | hello@willowmeredementia.bm</p>
      <p class="contact-line">(441) 555 0142</p>
    </div>
  </section>

</main>
</body>
</html>
```